Daily Care Record Sheets

As a preschool, we have notes that we send home on a daily basis so the parents know what is going on. We would like to reformat the preschool and toddler sheets<br/><br/>The preschool participation sheet is 4.25"x 5.6"<br/>We have attached an example of what we are using currently and the information we would like on our new sheet. We would like the logo added as well.<br/><br/>The Bramble Notes sheet should be a half page. I have included 2 examples as well as a sheet of what we would like on it moving forward. <br/><br/>Please do not hesitate to reach out if you have any questions on any of this. They will print in black and white on colored paper.<br/><br/>Thanks!<br/>Marla

Target Market(s)

Parents of the toddlers and preschools in our care

Industry/Entity Type

Preschool

Colors

Designer to choose only greyscale colors for use in the design.

Requirements
Must have
• Logo
• The items in the "FOR NEW VERSION" files

```html
<!DOCTYPE html>
<html lang="en">
<head>
<meta charset="utf-8">
<title>Preschool Participation – Brightfield Early Learning</title>
<link rel="stylesheet" href="https://fonts.googleapis.com/css2?family=Abel&family=Arimo:wght@400&family=Lato:wght@300&family=Oswald:wght@500&display=swap">
<style>
  :root {
    --ink: #111111;
    --paper: #ffffff;
    --rule: #1a1a1a;
    --muted: #333333;
  }
  * { box-sizing: border-box; margin: 0; padding: 0; }
  html, body { width: 911px; height: 1200px; overflow: hidden; background: var(--paper); }
  .sheet { position: relative; width: 911px; height: 1200px; color: var(--ink); font-family: "Abel", sans-serif; }
  .abs { position: absolute; }
  .center { transform: translate(-50%, -50%); white-space: nowrap; }
  .mid-y { transform: translateY(-50%); white-space: nowrap; }

  .brand-dot { left: 451px; top: 54px; width: 46px; height: 46px; border-radius: 50%; background: var(--ink); transform: translate(-50%, -50%); }
  .brand-name { left: 455px; top: 103px; font-family: "Lato", sans-serif; font-weight: 300; font-size: 40px; letter-spacing: -0.5px; }
  .brand-rule { left: 255px; top: 130px; width: 398px; height: 1px; background: var(--rule); }
  .brand-tagline { left: 455px; top: 140px; font-family: "Arimo", sans-serif; font-size: 8.5px; letter-spacing: 1.6px; }

  .sheet-title { left: 455px; top: 212px; font-family: "Oswald", sans-serif; font-weight: 500; font-size: 37px; transform: translate(-50%, -50%) scaleX(0.82); white-space: nowrap; }

  .field-label { font-family: "Oswald", sans-serif; font-weight: 500; font-size: 22px; transform: translateY(-50%) scaleX(0.8); transform-origin: left center; white-space: nowrap; }
  .rule { height: 1.5px; background: var(--rule); }

  .icon { width: 58px; height: 58px; transform: translate(-50%, -50%); }

  .card { width: 224px; height: 374px; top: 438px; border: 1.5px solid var(--ink); border-radius: 12px; overflow: hidden; }
  .card-head { height: 51px; background: var(--ink); color: var(--paper); font-family: "Arimo", sans-serif; font-size: 25px; display: flex; align-items: center; justify-content: center; letter-spacing: 0.3px; }
  .choice-lg { font-size: 29px; }
  .choice-sm { font-size: 19px; }
  .nap-multi { text-align: center; line-height: 38px; transform: translate(-50%, -50%); }
</style>
</head>
<body>
<main class="sheet">
  <header>
    <div class="abs brand-dot" aria-hidden="true"></div>
    <div class="abs center brand-name">Brightfield Early Learning</div>
    <div class="abs brand-rule"></div>
    <div class="abs center brand-tagline" style="top:143px">PRIVATE INFANT CARE · PRESCHOOL · ELEMENTARY · MIDDLE SCHOOL</div>
    <h1 class="abs sheet-title">PRESCHOOL PARTICIPATION</h1>
  </header>

  <section class="record-fields">
    <div class="abs field-label" style="left:54px; top:287px">CHILD:</div>
    <div class="abs rule" style="left:110px; top:306px; width:367px"></div>
    <div class="abs field-label" style="left:545px; top:281px">DATE:</div>
    <div class="abs rule" style="left:602px; top:299px; width:254px"></div>
  </section>

  <section class="daily-cards">
    <svg class="abs icon" style="left:167px; top:390px" viewBox="0 0 58 58" aria-label="Lunch icon">
      <circle cx="29" cy="29" r="29" fill="var(--ink)"/>
      <g fill="var(--paper)">
        <rect x="19" y="15" width="2" height="10"/><rect x="22.5" y="15" width="2" height="10"/><rect x="26" y="15" width="2" height="10"/>
        <rect x="19" y="24" width="9" height="4" rx="2"/><rect x="22" y="26" width="3" height="18" rx="1.5"/>
        <path d="M34 15 C40 17 40 27 37 30 L37 44 L34 44 Z"/>
      </g>
    </svg>
    <svg class="abs icon" style="left:454px; top:390px" viewBox="0 0 58 58" role="img" aria-label="Disposition icon of a child">
      <circle cx="29" cy="29" r="29" fill="var(--ink)"/>
    </svg>
    <svg class="abs icon" style="left:738px; top:390px" viewBox="0 0 58 58" aria-label="Nap time icon">
      <circle cx="29" cy="29" r="29" fill="var(--ink)"/>
      <path d="M30 13 A16 16 0 1 0 44 38 A13 13 0 1 1 30 13 Z" fill="var(--paper)"/>
      <circle cx="38" cy="20" r="2" fill="var(--paper)"/><circle cx="43" cy="29" r="1.6" fill="var(--paper)"/>
    </svg>

    <article class="abs card" style="left:54px">
      <h2 class="card-head">LUNCH</h2>
    </article>
    <div class="abs center choice-lg" style="left:166px; top:536px">ALL</div>
    <div class="abs center choice-lg" style="left:166px; top:609px">MOST</div>
    <div class="abs center choice-lg" style="left:166px; top:680px">SOME</div>
    <div class="abs center choice-lg" style="left:166px; top:753px">NONE</div>

    <article class="abs card" style="left:342px">
      <h2 class="card-head">DISPOSITION</h2>
    </article>
    <div class="abs mid-y choice-sm" style="left:370px; top:524px">Happy</div>
    <div class="abs mid-y choice-sm" style="left:466px; top:524px">Quiet</div>
    <div class="abs mid-y choice-sm" style="left:370px; top:571px">Curious</div>
    <div class="abs mid-y choice-sm" style="left:466px; top:571px">Talkative</div>
    <div class="abs mid-y choice-sm" style="left:370px; top:620px">Friendly</div>
    <div class="abs mid-y choice-sm" style="left:466px; top:620px">Cheerful</div>
    <div class="abs mid-y choice-sm" style="left:370px; top:668px">Sleepy</div>
    <div class="abs mid-y choice-sm" style="left:466px; top:668px">Energetic</div>
    <div class="abs center choice-sm" style="left:454px; top:722px">Mischievous</div>
    <div class="abs center choice-sm" style="left:454px; top:771px">Followed Directions</div>

    <article class="abs card" style="left:628px">
      <h2 class="card-head">NAP TIME</h2>
    </article>
    <div class="abs center choice-lg" style="left:740px; top:548px">I Slept Well</div>
    <div class="abs center choice-lg" style="left:740px; top:621px">I was Quiet</div>
    <div class="abs nap-multi choice-lg" style="left:740px; top:711px">I didn't feel like<br>resting</div>
  </section>

  <section class="notes">
    <div class="abs field-label" style="left:54px; top:887px">TODAY I HAD FUN:</div>
    <div class="abs rule" style="left:55px; top:946px; width:798px"></div>
    <div class="abs field-label" style="left:54px; top:1012px">NOTES/REMINDERS:</div>
    <div class="abs rule" style="left:55px; top:1071px; width:798px"></div>
    <div class="abs rule" style="left:55px; top:1131px; width:798px"></div>
  </section>
</main>
</body>
</html>
```